Silver Birch Decorators Banner

Create a banner that displays and reinforces Silver Birch Decorators’ brand identity while promoting our interior painting services. The banner will be displayed at indoor venues through the winter. The design should be clean, professional, and visually recognizable to both new and returning customers. See attached design brief & logo source files.

```html
<!DOCTYPE html>
<html lang="en">
<head>
<meta charset="utf-8">
<title>Silver Birch Decorators – Interior Painting Banner</title>
<link rel="stylesheet" href="https://fonts.googleapis.com/css2?family=Fraunces:opsz,wght@9..144,500;9..144,600&family=Josefin+Sans:wght@600;700&display=swap">
<style>
  :root {
    --page-bg: #e4e5e0;
    --banner-bg: #efefe9;
    --paint-green: #4f8a3b;
    --title-green: #4c8639;
    --light-text: #f4f4ee;
    --dark-text: #3b3b37;
    --url-bar: #3a3a36;
    --figure-tone: #d98a3a;
  }
  * { margin: 0; padding: 0; box-sizing: border-box; }
  html, body { width: 1200px; height: 1200px; overflow: hidden; background: var(--page-bg); }
  .banner {
    position: absolute; left: 0; top: 372px;
    width: 1200px; height: 456px;
    background: var(--banner-bg);
    overflow: hidden;
  }
  .paint-splash { position: absolute; left: 150px; top: 0; width: 500px; height: 440px; }
  .painter-figure {
    position: absolute; left: 88px; top: 28px; width: 220px; height: 414px;
    background: linear-gradient(180deg, var(--figure-tone) 0%, #2f8f86 60%, #2a6e68 100%);
    border-radius: 90px 90px 20px 20px;
    opacity: .85;
  }
  .headline {
    position: absolute; left: 310px; top: 70px;
    font-family: "Fraunces", serif; font-weight: 600;
    font-size: 150px; line-height: 1; letter-spacing: 2px;
    background: linear-gradient(90deg, var(--light-text) 0 48%, var(--title-green) 48% 100%);
    -webkit-background-clip: text; background-clip: text;
    color: transparent;
  }
  .subhead {
    position: absolute; left: 382px; top: 218px;
    font-family: "Fraunces", serif; font-weight: 500; font-size: 50px; line-height: 1;
  }
  .subhead .on-paint { color: var(--light-text); }
  .subhead .on-light { color: var(--dark-text); }
  .brand-name {
    position: absolute; left: 950px; top: 300px; width: 170px;
    display: flex; align-items: center; gap: 10px;
    font-family: "Josefin Sans", sans-serif; font-weight: 700; font-size: 19px; line-height: 1.1;
    color: var(--paint-green); text-transform: uppercase;
  }
  .brand-name .mark { width: 22px; height: 22px; background: var(--paint-green); flex: none; }
  .cta {
    position: absolute; left: 617px; top: 386px; height: 34px;
    display: flex; align-items: center;
    font-family: "Josefin Sans", sans-serif; font-weight: 600; font-size: 21px; color: var(--dark-text);
  }
  .cta .url {
    margin-left: 8px; height: 34px; padding: 6px 14px 0;
    background: var(--url-bar); color: var(--light-text);
    width: 300px;
  }
</style>
</head>
<body>
  <section class="banner">
    <svg class="paint-splash" viewBox="0 0 500 440" role="img" aria-label="Dripping green paint swath">
      <path fill="var(--paint-green)" d="M20 0 H480 V300 C478 340 450 350 430 330 C410 380 360 420 320 400 C280 430 250 380 230 410 C200 440 170 400 160 360 C140 340 120 300 110 260 C90 230 60 200 40 150 C25 110 20 60 20 0 Z"/>
    </svg>
    <div class="painter-figure" role="img" aria-label="Illustrated painter in orange shirt and teal overalls rolling green paint"></div>
    <h1 class="headline">INTERIOR</h1>
    <p class="subhead"><span class="on-paint">Painting</span> <span class="on-light">Services</span></p>
    <div class="brand-name"><span class="mark"></span><span>Silver Birch Decorators</span></div>
    <p class="cta">Book a Free Estimate at <span class="url">www.silverbirchdecor.com</span></p>
  </section>
</body>
</html>
```